Here is the link where the current banner is featured https://www.brimkit.com.au/collections/gel-blasters

I need the banner recreated into desktop and mobile format size.
Update the key points to:
- FREE SHIPPING AUSTRALIA WIDE
- SAME DAY DISPATCH
- BEST PRICE GUARANTEE
- 3000+ 5 STAR REVIEWS
- BEST SERVICE & WARRANTY
- 100% SECURE CHECKOUT

I want the banner to suit the style of the website and make it look better than the last graphic.

I also need the "save even more" picture to be recreated as it looks very plain at the moment,

```html
<!DOCTYPE html>
<html lang="en">
<head>
<meta charset="utf-8">
<title>Brimkit – Why Shop With Us</title>
<link rel="stylesheet" href="https://fonts.googleapis.com/css2?family=Open+Sans:wght@700&display=swap">
<style>
  :root {
    --page: #ffffff;
    --banner-dark: #0b0b0c;
    --banner-mid: #1c1c1e;
    --badge: #ffffff;
    --label: #ffffff;
    --accent: #e31b23;
    --truck: #e31b23;
    --money: #2aa53a;
    --star: #f5b50a;
    --thumb: #1aa7e6;
    --shield: #9a9a9a;
    --map-blue: #1f3f8f;
  }
  html, body {
    margin: 0;
    width: 1200px;
    height: 262px;
    overflow: hidden;
    background: var(--page);
  }
  .canvas {
    position: relative;
    width: 1200px;
    height: 262px;
  }
  .trust-banner {
    position: absolute;
    left: 21px;
    top: 43px;
    width: 1157px;
    height: 176px;
    box-shadow: 0 8px 14px rgba(0, 0, 0, 0.28);
    overflow: hidden;
  }
  .banner-photo {
    position: absolute;
    inset: 0;
    background:
      radial-gradient(ellipse 40% 70% at 22% 40%, rgba(60,60,62,0.55), transparent 70%),
      radial-gradient(ellipse 35% 60% at 55% 35%, rgba(50,50,52,0.5), transparent 70%),
      radial-gradient(ellipse 30% 60% at 85% 55%, rgba(45,45,47,0.45), transparent 70%),
      linear-gradient(90deg, var(--banner-dark), var(--banner-mid) 50%, var(--banner-dark));
  }
  .feature {
    position: absolute;
    top: 52px;
    width: 120px;
    margin-left: -60px;
    text-align: center;
    font-family: "Open Sans", sans-serif;
    font-weight: 700;
    font-size: 7.4px;
    line-height: 9px;
  }
  .feature-badge {
    width: 54px;
    height: 54px;
    margin: 0 auto 5px;
    border-radius: 50%;
    background: var(--badge);
    display: flex;
    align-items: center;
    justify-content: center;
  }
  .feature-badge svg { display: block; }
  .feature-title { color: var(--label); display: block; }
  .feature-sub { color: var(--accent); display: block; }
  .dollar {
    font-family: "Open Sans", sans-serif;
    font-weight: 700;
    font-size: 44px;
    line-height: 1;
    color: var(--money);
  }
</style>
</head>
<body>
<div class="canvas">
  <section class="trust-banner">
    <div class="banner-photo" role="img" aria-label="Dark moody photograph of tactical gear: a rifle, handheld radio, binoculars and a patch on a vest"></div>

    <div class="feature" style="left:255px">
      <div class="feature-badge">
        <svg width="46" height="42" viewBox="0 0 46 42" role="img" aria-label="Map of Australia in the national flag colours">
          <ellipse cx="23" cy="20" rx="22" ry="17" fill="var(--map-blue)"/>
        </svg>
      </div>
      <span class="feature-title">FREE SHIPPING</span>
      <span class="feature-sub">AUSTRALIA WIDE</span>
    </div>

    <div class="feature" style="left:388px">
      <div class="feature-badge">
        <svg width="42" height="28" viewBox="0 0 42 28" aria-hidden="true">
          <rect x="0" y="2" width="26" height="18" fill="var(--truck)"/>
          <path d="M27 7 h8 l6 7 v6 h-14 z" fill="var(--truck)"/>
          <path d="M30 9 h4 l4 5 h-8 z" fill="#fff"/>
          <circle cx="9" cy="22" r="4" fill="var(--truck)" stroke="#fff" stroke-width="1.5"/>
          <circle cx="33" cy="22" r="4" fill="var(--truck)" stroke="#fff" stroke-width="1.5"/>
        </svg>
      </div>
      <span class="feature-title">SAME DAY</span>
      <span class="feature-sub">DISPATCH</span>
    </div>

    <div class="feature" style="left:513px">
      <div class="feature-badge"><span class="dollar">$</span></div>
      <span class="feature-title">BEST PRICE</span>
      <span class="feature-sub">GUARANTEE</span>
    </div>

    <div class="feature" style="left:635px">
      <div class="feature-badge">
        <svg width="46" height="9" viewBox="0 0 46 9" aria-hidden="true" fill="var(--star)">
          <path id="s" d="M4.5 0 l1.1 3 h3.2 l-2.6 1.9 1 3.1 -2.7 -1.9 -2.7 1.9 1 -3.1 -2.6 -1.9 h3.2 z"/>
          <use href="#s" x="9.3"/><use href="#s" x="18.6"/><use href="#s" x="27.9"/><use href="#s" x="37.2"/>
        </svg>
      </div>
      <span class="feature-title">3000+ 5 STAR</span>
      <span class="feature-sub">REVIEWS</span>
    </div>

    <div class="feature" style="left:764px">
      <div class="feature-badge">
        <svg width="30" height="28" viewBox="0 0 30 28" aria-hidden="true" fill="var(--thumb)">
          <rect x="0" y="11" width="6" height="15"/>
          <path d="M8 11 l6 -6 1 -5 q4 0 4 5 l-1 5 h9 q3 0 3 3 l-2 10 q-1 3 -4 3 h-16 z"/>
        </svg>
      </div>
      <span class="feature-title">BEST</span>
      <span class="feature-sub">SERVICE &amp; WARRANTY</span>
    </div>

    <div class="feature" style="left:898px">
      <div class="feature-badge">
        <svg width="28" height="34" viewBox="0 0 28 34" aria-hidden="true">
          <path d="M14 0 l14 5 v10 q0 12 -14 19 q-14 -7 -14 -19 v-10 z" fill="var(--shield)"/>
          <path d="M10 15 v-3 a4 4 0 0 1 8 0 v3" fill="none" stroke="#fff" stroke-width="2"/>
          <rect x="8" y="15" width="12" height="10" rx="1" fill="#fff"/>
          <rect x="13" y="18" width="2" height="4" fill="var(--shield)"/>
        </svg>
      </div>
      <span class="feature-title">100% SECURE</span>
      <span class="feature-sub">CHECKOUT</span>
    </div>
  </section>
</div>
</body>
</html>
```